Brennick Setter Club - Rare dog breed club needs web design!

The Transylvanian Hound (or Erdélyi kopó) is an ancient Hungarian dog breed. These medium-sized hounds were favored by the Hungarian kings and princes for hunting bears and wolves in the Carpathian mountains of Transylvania. The breed's great adaptability to the region's extreme climates of sweltering summers and frigid winters made it an excellent all season hunting dog. This dog has a sleek appearance and stunning good looks. They are lean, appear very elegant and proud. Their erect posture and beautifully sculpted head portray great attentiveness and authority. In general, this rare breed is extremely good natured, loyal and obedient. It has a tendency to form strong attachments to its primary caretakers and will remain loyal and protective. (Please refer to existing web resources.)

The Brennick Setter Club - with current website www.brennicksetter.com - is the official breed club of Transylvanian Hound afficionados, breeders and owners in the United States, which was founded in 2010. We are looking for a web design for the new, upgraded version of this central (currenty non-functioning) website. Please do not recycle the old logo (we may choose from your suggesions and pay for it!) or any of the old texts. Please use the structure described below. Overall, the webpage serves a dual purpose: an educational one (about the breed itself) and a community-building one (inside the Club). The proposed structure of the website is as follows:

1. About the Kopó
- Breed History
- Breed Standard
- Public Education
- Photo Gallery

2. Life with a Kopó
- Health and Genetics
- Feeding and Nutrition
- Training and Activities

3. Finding a Kopó
- Is this the Right Breed for You?
- Choosing a Puppy
- FAQ
- Breeder Referral

4. The Brennick Setter Club
- Constituton
- Officers and Appointees
- Code of Ethics
- Breeder Guidelines
- Membership
- Reports
- Links

5. News and Events

6. Shop

We are attaching a couple of examples of the graphics/drawings of the dogs that would be part of the design of the website. We plan to have more of these artistic depictions, nicely embedded into the background (maybe shaded out at the edges just like the drawings themselves) and less actual photos. Or a good combination of the two.

Further information upon request.

Reason: There are a few very promising design collaborations ongoing. As we moved the brief to a more artistic and graphic direction, we felt that one week of extension would be needed to get to the perfect end-product, which could include designs for sub-pages as well.

Reason: In order to make the final modifications to the leading designs, and at the request of those designers, the deadline is extended until Friday.

Target Market(s)

- BRSC Club members, dog (especially T-Hound) owners, past and future owners, breeders, puppy buyers, hunters, kennel clubs, dog show participants, vets, animal shelters, Hungarian, Romanian and other European web visitors, historians

Industry/Entity Type

Club

Font styles to use
Serif
Decorative
Script

Requirements
Must have
• - Sync with graphics of dogs (see attachments), but accentuate the rich black basic color of the dogs
- Elegance, aristocratic/noble look and feel (but not overly archaic)
- Love, companionship, dogs as family members
- Hunting usage, but no bloody associations, rather romantic ones
- Simple to use and navigate for non-web-natives
- Old world (Central European) atmosphere, even the exotic, rustic and romantic Transylvanian feel - SEE the new attachment for inspiration (this was a design plan which we discarded (mainly because of its gothic, (nazi-like), unreadable font, and the fact that the plan makes the black-looking dogs appear brown), however we loved the fact that it was not full of boxes/windows, had a marble/sand stone like continuous background, lots of little elegant graphics, the drawings embedded, etc.
Nice to have
• - Working on smartphone, Zentabs, etc., so dynamic website design
- Web shop to be added to functionalities in the future (?)
- English language for now, in the future can be Hungarian, Romanian, etc., so the font choice should handle various alphabets
- Focus on the dogs (likely more graphics than photos, at least on the main pages), and not on the activities/humans - the design should accentuate the black and not the tan of the graphics!
Should not have
• - Old logo from the old www.brennicksetter.com webpage or the other logo from the Chatterly site of the Brennick Setter Club, we will have a new one (maybe designed by you!)
- Breed club, kennel club cliches
- Cutesy, adorable, cheesy design elements
- Old, stale, monolithic, archaic, snobbish, etc. look and feel
- No vampire associations

```html
<!DOCTYPE html>
<html lang="en">
<head>
<meta charset="utf-8">
<title>The Brennick Setter Club</title>
<link rel="stylesheet" href="https://fonts.googleapis.com/css2?family=Tinos:ital,wght@0,400;0,700;1,400&family=Mako&display=swap">
<style>
  :root {
    --paper: #ffffff;
    --ink: #000000;
    --band: #c4bda7;
    --nav-active: #ffffff;
    --accent-red: #d21f2b;
    --art-dark: #4a3a33;
    --art-tan: #a98a72;
    --art-light: #d6cfbf;
    --photo-straw: #cdb988;
    --photo-sky: #6aa6de;
    --photo-dark: #3a302a;
    --footer: #000000;
    --footer-text: #ffffff;
  }
  * { margin: 0; padding: 0; box-sizing: border-box; }
  html, body {
    width: 1186px; height: 1200px; overflow: hidden;
    background: var(--paper);
  }
  .page {
    position: relative; width: 1186px; height: 1200px;
    font-family: "Mako", "Candara", sans-serif;
    color: var(--ink);
  }
  .brand { position: absolute; left: 43px; top: 42px; display: flex; align-items: center; }
  .brand-mark {
    width: 79px; height: 68px; border-radius: 50%;
    background: var(--ink); color: var(--paper);
    font-family: "Tinos", "Times New Roman", serif; font-size: 36px;
    display: flex; align-items: center; justify-content: center;
    padding-bottom: 4px;
  }
  .brand-name {
    margin-left: 23px;
    font-family: "Tinos", "Times New Roman", serif; font-style: italic;
    font-size: 37px; font-weight: 400;
  }
  .hero-band {
    position: absolute; left: 0; top: 157px; width: 1186px; height: 455px;
    background: var(--band);
  }
  .hero-art {
    position: absolute; left: 562px; top: 81px; width: 574px; height: 547px;
    background: linear-gradient(180deg,
      var(--art-dark) 0%,
      var(--art-tan) 45%,
      var(--art-light) 80%,
      var(--paper) 100%);
  }
  .main-nav {
    position: absolute; left: 51px; top: 231px;
    list-style: none;
    font-family: "Tinos", "Times New Roman", serif; font-size: 29px;
  }
  .main-nav li { height: 64.5px; }
  .main-nav a { color: var(--ink); text-decoration: none; }
  .main-nav .is-active a { color: var(--nav-active); }

  .topic { position: absolute; left: 36px; width: 530px; height: 120px; }
  .topic-photo { position: absolute; left: 0; top: 0; width: 234px; height: 120px; }
  .photo-straw { background: linear-gradient(90deg, var(--photo-straw) 0%, #b9a57a 50%, #e3d6ad 100%); }
  .photo-sky { background: linear-gradient(90deg, var(--photo-sky) 0%, #4f6f8e 50%, var(--photo-dark) 100%); }
  .topic-title {
    position: absolute; left: 257px; top: -4px;
    font-family: "Tinos", "Times New Roman", serif; font-weight: 700; font-size: 23px;
  }
  .topic-text {
    position: absolute; left: 257px; top: 45px; width: 272px;
    font-size: 17px; line-height: 23px;
  }
  .read-more {
    position: absolute; left: 454px; top: 94px;
    font-family: "Tinos", "Times New Roman", serif; font-size: 15px;
    color: var(--accent-red); text-decoration: none;
  }

  .intro { position: absolute; left: 615px; top: 668px; width: 512px; }
  .intro h1 {
    font-family: "Tinos", "Times New Roman", serif; font-weight: 400;
    font-size: 35px; line-height: 43px; margin-bottom: 50px;
  }
  .intro p { font-size: 17px; line-height: 23px; margin-bottom: 23px; }
  .intro p.spaced { margin-top: 34px; }

  .site-footer {
    position: absolute; left: 0; top: 1147px; width: 1186px; height: 53px;
    background: var(--footer); color: var(--footer-text);
    font-family: "Tinos", "Times New Roman", serif; font-size: 13px;
    display: flex; align-items: center; justify-content: center;
  }
</style>
</head>
<body>
<div class="page">
  <header class="brand">
    <div class="brand-mark">logo</div>
    <div class="brand-name">The Brennick Setter Club</div>
  </header>

  <div class="hero-band"></div>
  <div class="hero-art" role="img" aria-label="Pastel drawing of a hound's head"></div>

  <nav>
    <ul class="main-nav">
      <li class="is-active"><a href="#">About the Kopo</a></li>
      <li><a href="#">Life with a Kopó</a></li>
      <li><a href="#">The Brennick Setter Club</a></li>
      <li><a href="#">News and Events</a></li>
      <li><a href="#">Shop</a></li>
    </ul>
  </nav>

  <section class="topic" style="top:684px">
    <div class="topic-photo photo-straw" role="img" aria-label="Photo of a hound resting in tall dry grass"></div>
    <h2 class="topic-title">Topic 1 About</h2>
    <p class="topic-text">Text describing topic 1.Text describing topic 1.Text describing topic 1.</p>
    <a class="read-more" href="#">Read More</a>
  </section>
  <section class="topic" style="top:818px">
    <div class="topic-photo photo-sky" role="img" aria-label="Photo of a hound against a blue sky"></div>
    <h2 class="topic-title">Topic 2 About</h2>
    <p class="topic-text">Text describing topic 2.Text describing topic 2.Text describing topic 2.</p>
    <a class="read-more" href="#">Read More</a>
  </section>
  <section class="topic" style="top:956px">
    <div class="topic-photo photo-straw" role="img" aria-label="Photo of a hound resting in tall dry grass"></div>
    <h2 class="topic-title">Topic 3 About</h2>
    <p class="topic-text">Text describing topic 3.Text describing topic 3.Text describing topic 3.</p>
    <a class="read-more" href="#">Read More</a>
  </section>

  <article class="intro">
    <h1>Main Descriptive Text<br>About the Hound</h1>
    <p>Main Descriptive Text About the HoundMain Descriptive Text About the HoundMain Descriptive Text About the HoundMain Descriptive Text About the Hound.</p>
    <p>Main Descriptive Text About the HoundMain Descriptive Text About the HoundMain Descriptive Text About the Hound.</p>
    <p class="spaced">Main Descriptive Text About the Hound.</p>
    <p>Main Descriptive Text About the Hound.Main Descriptive Text About the Hound.Main Descriptive Text About the Hound.Main Descriptive Text About the Hound.</p>
  </article>

  <footer class="site-footer">Copyright : etc.</footer>
</div>
</body>
</html>
```